Business Card Design Project

Keep it simple , using logo and colors that compliment. Logo on one side with complimentary back ground color. Other side, personal info with possible complimentary design/colors

Target Market(s)

we are a non for profit that will be seeking donations . Both monetary and in kind

Industry/Entity Type

Business

Font styles to use
Sans Serif

Colors

Designer to choose colors to be used in the design.

```html
<!DOCTYPE html>
<html lang="en">
<head>
<meta charset="utf-8">
<title>Open Field Fund – Business Card</title>
<link href="https://fonts.googleapis.com/css2?family=Arimo:wght@400&display=swap" rel="stylesheet">
<style>
  :root {
    --navy: #2c3457;
    --yellow: #fff212;
    --icon-blue: #00aeef;
    --paper: #fdfdfd;
    --edge: #8a8a8a;
  }
  * { margin: 0; padding: 0; box-sizing: border-box; }
  html, body { width: 976px; height: 1200px; overflow: hidden; background: #ffffff; }
  body { position: relative; font-family: "Arimo", Arial, sans-serif; }

  .card { position: absolute; left: 0; width: 976px; height: 555px; }
  .card--front { top: 0; }
  .card--back { top: 645px; }
  .card-shape { position: absolute; inset: 0; width: 100%; height: 100%; }

  .brand-mark {
    position: absolute;
    border-radius: 50%;
    display: flex; align-items: center; justify-content: center;
    text-align: center;
    color: var(--yellow);
    font-weight: 400;
    line-height: 1.05;
  }
  .brand-mark--large {
    left: 336px; top: 125px; width: 304px; height: 304px;
    background: var(--navy);
    border: 11px solid var(--yellow);
    font-size: 50px;
  }
  .brand-mark--small {
    left: 687px; top: 58px; width: 148px; height: 148px;
    border: 5px solid var(--yellow);
    font-size: 24px;
  }

  .contact {
    position: absolute; left: 80px; top: 310px;
    list-style: none;
    color: #ffffff;
    font-size: 21px;
  }
  .contact li { display: flex; align-items: center; height: 34px; }
  .contact .icon { width: 18px; height: 18px; margin-right: 8px; flex: none; }
  .contact .icon-spacer { width: 18px; margin-right: 8px; flex: none; }
</style>
</head>
<body>

<section class="card card--front">
  <svg class="card-shape" viewBox="0 0 976 555" aria-hidden="true">
    <path d="M57,0.5 H919 Q945,0.5 950,25 Q975.5,150 975.5,277.5 Q975.5,405 950,530 Q945,554.5 919,554.5 H57 Q31,554.5 26,530 Q0.5,405 0.5,277.5 Q0.5,150 26,25 Q31,0.5 57,0.5 Z"
          fill="var(--paper)" stroke="var(--edge)" stroke-width="1"/>
  </svg>
  <div class="brand-mark brand-mark--large">Open<br>Field<br>Fund</div>
</section>

<section class="card card--back">
  <svg class="card-shape" viewBox="0 0 976 555" aria-hidden="true">
    <path d="M57,0 H919 Q945,0 950,25 Q976,150 976,277.5 Q976,405 950,530 Q945,555 919,555 H57 Q31,555 26,530 Q0,405 0,277.5 Q0,150 26,25 Q31,0 57,0 Z"
          fill="var(--navy)"/>
  </svg>
  <div class="brand-mark brand-mark--small">Open<br>Field<br>Fund</div>

  <ul class="contact">
    <li><span class="icon-spacer"></span>Dan &amp; Laura Hewitt</li>
    <li>
      <svg class="icon" viewBox="0 0 18 18" aria-hidden="true"><path d="M9 1a6 6 0 0 0-6 6c0 4.5 6 10 6 10s6-5.5 6-10a6 6 0 0 0-6-6zm0 8.3a2.3 2.3 0 1 1 0-4.6 2.3 2.3 0 0 1 0 4.6z" fill="var(--icon-blue)"/></svg>
      4120 Prairie Lane, Oakvale, Minnesota 56000.
    </li>
    <li>
      <svg class="icon" viewBox="0 0 18 18" aria-hidden="true"><path d="M2 7c0-2 3-3.5 7-3.5S16 5 16 7v1h-3.5V6.5h-7V8H2z M5 9h8l2 6H3z" fill="var(--icon-blue)"/><circle cx="9" cy="12" r="1.8" fill="var(--navy)"/></svg>
      555-010-2233 (H) 555-010-4477 (C)
    </li>
    <li>
      <svg class="icon" viewBox="0 0 18 18" aria-hidden="true"><rect x="1" y="4" width="16" height="11" fill="var(--icon-blue)"/><path d="M1 4l8 6 8-6" fill="none" stroke="var(--navy)" stroke-width="1.3"/></svg>
      hello@openfieldfund.org
    </li>
    <li>
      <svg class="icon" viewBox="0 0 18 18" aria-hidden="true"><g fill="none" stroke="var(--icon-blue)" stroke-width="1.2"><circle cx="9" cy="9" r="7.5"/><ellipse cx="9" cy="9" rx="3.3" ry="7.5"/><path d="M1.5 9h15M2.8 5h12.4M2.8 13h12.4"/></g></svg>
      www.openfieldfund.org
    </li>
  </ul>
</section>

</body>
</html>
```